Cutting Edge Property Services Provider is Looking to Update Business Card Design

We are looking to freshen up our business cards to match our cutting edge technology based image.

QUANDO-VAX - Where Care Finds Progress

More information about our company can be found on our website at www.quando-vax.example

We integrate technology in a historically low tech industry.

We have appeared on the Ledger 300/3000 list 2 years in a row and we're previously recognized as the 5th Fastest Growing Company in San Diego.

Our core colors are blue and white, but are not against accents that might improve our image.

We currently have our Mission Statement on our Business Cards in a folding design:
QUANDO-VAX IS THE LEADING BUILDING SERVICES INNOVATOR. BY COMBINING TECHNOLOGY WITH FUNCTIONAL TOOS THAT IMPROVE EFFICIENCY IN THE WORKPLACE, WE PROVIDE UNPARALLELED SERVICE IN THE INDUSTRY. DEVELOPING LASTING RELATIONSHIPS WITH OUR CLIENTS AND ASSOCIATES IS THE CORNERSTONE OF OUR SUCCESS.

We'd like to convey the image of a cutting edge, technology based company. Want the cards to pop.

Target Market(s)

Commercial Property Managers - 20 to 50 year old professionals

Industry/Entity Type

Business

Requirements
Must have
• Must utilize our logo obviously, but are definitely open to using variations on the logo. Utilizing the components of the logo, but maybe in different configurations or backgrounds, etc...

Must use the Name: QUANDO-VAX.
Can also use QUANDO-VAX PROPERTY SERVICES.

Must include the Mission Statement

Must say: Where Care Finds Progress
Nice to have
• We are considering plastic stock, shaped cards, or folding cards.

Nothing over the top or really expensive, but will consider if it conveys innovation and technology.
Should not have
• No images of toilets, buildings, trees, or anything relating to commercial properties.

We want to convey our technology image.

```html
<!DOCTYPE html>
<html lang="en">
<head>
<meta charset="utf-8">
<title>QUANDO-VAX Business Card</title>
<link href="https://fonts.googleapis.com/css2?family=Roboto+Condensed:ital,wght@0,400;0,700;1,400&family=Roboto:ital,wght@0,300;0,400;1,300&display=swap" rel="stylesheet">
<style>
  :root {
    --page: #e7e7e5;
    --navy: #0d4a7c;
    --navy-deep: #0a416f;
    --orange: #ee5a2c;
    --white: #ffffff;
    --ink-grey: #6e6e6e;
    --rule: #d4d4d4;
  }
  * { margin: 0; padding: 0; box-sizing: border-box; }
  html, body { width: 1108px; height: 1200px; overflow: hidden; background: var(--page); }
  .canvas { position: relative; width: 1108px; height: 1200px; }

  .card { position: absolute; left: 101px; width: 905px; height: 514px; box-shadow: 0 6px 18px rgba(0,0,0,.18); }

  /* Front: mission side */
  .card--mission { top: 62px; background: var(--navy); border-radius: 66px 66px 66px 0; }
  .mission-brand { position: absolute; left: 38px; top: 176px; width: 262px; display: flex; align-items: center; gap: 14px; }
  .brand-square { width: 26px; height: 26px; background: var(--white); flex: none; }
  .brand-name { font-family: "Roboto Condensed", sans-serif; font-weight: 700; font-size: 40px; letter-spacing: 1px; color: var(--white); line-height: 1; }
  .mission-divider { position: absolute; left: 333px; top: 128px; width: 2px; height: 296px; background: rgba(255,255,255,.75); }
  .mission-text { position: absolute; left: 368px; top: 134px; font-family: "Roboto Condensed", sans-serif; font-size: 24.5px; line-height: 36px; letter-spacing: .6px; color: var(--white); white-space: nowrap; }
  .mission-text .accent { color: var(--orange); font-weight: 700; }

  /* Back: contact side */
  .card--contact { top: 624px; background: var(--white); border-radius: 0 66px 0 66px; }
  .person-name { position: absolute; left: 43px; top: 80px; font-family: "Roboto Condensed", sans-serif; font-weight: 700; font-size: 43px; color: var(--navy); }
  .person-role { position: absolute; left: 43px; top: 128px; font-family: "Roboto", sans-serif; font-style: italic; font-weight: 300; font-size: 20px; color: var(--ink-grey); }
  .rule { position: absolute; left: 38px; width: 426px; height: 2px; background: var(--rule); }
  .rule--top { top: 176px; }
  .rule--bottom { top: 358px; }
  .contact-list { position: absolute; left: 43px; top: 196px; list-style: none; }
  .contact-list li { display: flex; align-items: center; height: 36.5px; font-family: "Roboto", sans-serif; font-weight: 300; font-size: 21.5px; color: var(--ink-grey); }
  .contact-list svg { width: 16px; height: 16px; margin-right: 21px; fill: var(--navy); flex: none; }
  .address { position: absolute; left: 43px; top: 380px; display: flex; gap: 14px; font-family: "Roboto", sans-serif; font-weight: 300; font-size: 21.5px; line-height: 36px; color: var(--ink-grey); }
  .address svg { width: 22px; height: 30px; fill: var(--navy); margin-top: 18px; flex: none; }

  .contact-brand { position: absolute; left: 480px; top: 172px; width: 420px; display: flex; justify-content: center; align-items: center; gap: 14px; }
  .contact-brand .brand-square { background: var(--navy); width: 28px; height: 28px; }
  .contact-brand .brand-name { color: var(--navy); font-size: 46px; }
  .tagline { position: absolute; left: 480px; top: 266px; width: 420px; text-align: center; font-family: "Roboto", sans-serif; font-weight: 400; font-size: 21px; letter-spacing: .3px; color: var(--ink-grey); }
</style>
</head>
<body>
<div class="canvas">

  <section class="card card--mission">
    <div class="mission-brand">
      <span class="brand-square"></span>
      <span class="brand-name">QUANDO-VAX</span>
    </div>
    <div class="mission-divider"></div>
    <p class="mission-text"><span class="accent">QUANDO-VAX</span> IS THE LEADING BUILDING<br>SERVICES INNOVATOR. BY COMBINING<br>TECHNOLOGY WITH FUNCTIONAL TOOLS THAT<br>IMPROVE EFFICIENCY IN THE WORKPLACE,<br>WE PROVIDE UNPARALLELED SERVICE IN THE<br>INDUSTRY. DEVELOPING LASTING RELATION-<br>SHIPS WITH OUR CLIENTS AND ASSOCIATES<br>IS THE CORNERSTONE OF OUR SUCCESS.</p>
  </section>

  <section class="card card--contact">
    <h1 class="person-name">Name Surname</h1>
    <p class="person-role">manager</p>
    <div class="rule rule--top"></div>
    <ul class="contact-list">
      <li><svg viewBox="0 0 16 16" aria-hidden="true"><path d="M4 0h8a1 1 0 0 1 1 1v14a1 1 0 0 1-1 1H4a1 1 0 0 1-1-1V1a1 1 0 0 1 1-1zm1 2v7h6V2zm1 9v1.5h1.5V11zm2.5 0v1.5H10V11zM6 13.5V15h1.5v-1.5zm2.5 0V15H10v-1.5z"/></svg>+00 123 456 789</li>
      <li><svg viewBox="0 0 16 16" aria-hidden="true"><path d="M4 1h8v4H4zM1 6h14v7h-2v-3H3v3H1zm3 5h8v4H4z"/></svg>+00 123 456 789</li>
      <li><svg viewBox="0 0 16 16" aria-hidden="true"><path d="M0 3h16v1.2L8 9 0 4.2zm0 2.6 8 4.8 8-4.8V13H0z"/></svg>office@quando-vax.example</li>
      <li><svg viewBox="0 0 16 16" aria-hidden="true"><path d="M8 0a8 8 0 1 0 0 16A8 8 0 0 0 8 0zm-.7 1.6v3.1H5.2c.5-1.6 1.2-2.7 2.1-3.1zm1.4 0c.9.4 1.6 1.5 2.1 3.1H8.7zM4.6 2.3a9 9 0 0 0-.9 2.4H2.3a6.5 6.5 0 0 1 2.3-2.4zm6.8 0a6.5 6.5 0 0 1 2.3 2.4h-1.4a9 9 0 0 0-.9-2.4zM1.6 6.1h1.9a12 12 0 0 0 0 3.8H1.6a6.5 6.5 0 0 1 0-3.8zm3.3 0h2.4v3.8H4.9a11 11 0 0 1 0-3.8zm3.8 0h2.4a11 11 0 0 1 0 3.8H8.7zm3.8 0h1.9a6.5 6.5 0 0 1 0 3.8h-1.9a12 12 0 0 0 0-3.8zM2.3 11.3h1.4c.2.9.5 1.7.9 2.4a6.5 6.5 0 0 1-2.3-2.4zm2.9 0h2.1v3.1c-.9-.4-1.6-1.5-2.1-3.1zm3.5 0h2.1c-.5 1.6-1.2 2.7-2.1 3.1zm3.6 0h1.4a6.5 6.5 0 0 1-2.3 2.4c.4-.7.7-1.5.9-2.4z"/></svg>www.quando-vax.example</li>
    </ul>
    <div class="rule rule--bottom"></div>
    <div class="address">
      <svg viewBox="0 0 22 30" aria-hidden="true"><path d="M11 0C4.9 0 0 4.9 0 11c0 7.5 11 19 11 19s11-11.5 11-19C22 4.9 17.1 0 11 0zm0 15.5a4.5 4.5 0 1 1 0-9 4.5 4.5 0 0 1 0 9z"/></svg>
      <p>1250 Harbor Crest Ave. Suite 210<br>San Diego, CA 92101</p>
    </div>

    <div class="contact-brand">
      <span class="brand-square"></span>
      <span class="brand-name">QUANDO-VAX</span>
    </div>
    <p class="tagline">WHERE CARE FINDS PROGRESS</p>
  </section>

</div>
</body>
</html>
```